TalkBloom - Language Coaching Services

Sleek, innovative, trendy design for Language Coaching business.

TalkBloom is a new UK based company that provides Language Coaching services. We offer highly personalized on-line and face to face language courses. We also impart learning techniques workshops based on the latest neuroscience research for second-language acquisition.

Target Market(s)

Industry/Entity Type

Consulting

Contact Information for Business Card

TalkBloom
DaniraQT@talkbloom.co.uk
TalkBloom.co.uk
London, UK

Font styles to use
Sans Serif

```html
<!DOCTYPE html>
<html lang="en">
<head>
<meta charset="utf-8">
<title>TalkBloom – Business Cards</title>
<link rel="stylesheet" href="https://fonts.googleapis.com/css2?family=Montserrat:wght@400;700&family=Roboto:wght@400&display=swap">
<style>
  :root {
    --bg: #2b2b2d;
    --brand-blue: #1b7fbf;
    --brand-blue-deep: #045d8f;
    --brand-blue-bright: #1fa8e0;
    --soft-blue: #dcecf6;
    --ink-grey: #4a4a4a;
    --muted-grey: #9a9a9a;
    --white: #ffffff;
  }
  * { margin: 0; padding: 0; box-sizing: border-box; }
  html, body { width: 1200px; height: 960px; overflow: hidden; background: var(--bg); }
  .canvas { position: relative; width: 1200px; height: 960px; }

  .card {
    position: absolute;
    width: 560px;
    height: 320px;
    border-radius: 3px;
    overflow: hidden;
    box-shadow: 0 14px 30px rgba(0,0,0,0.45);
  }

  /* Reverse side */
  .card-back {
    left: 80px; top: 120px;
    background: radial-gradient(ellipse at 45% 40%, var(--brand-blue-bright) 0%, var(--brand-blue) 45%, var(--brand-blue-deep) 100%);
    display: flex; flex-direction: column; align-items: center; justify-content: center; gap: 18px;
  }
  .back-mark {
    width: 74px; height: 74px; border-radius: 50%;
    border: 4px solid var(--white);
  }
  .back-wordmark {
    font-family: "Montserrat", sans-serif;
    font-weight: 700; font-size: 38px; letter-spacing: 2px;
    color: var(--white);
  }

  /* Front side */
  .card-front {
    left: 560px; top: 440px;
    background: var(--white);
  }
  .front-decoration {
    position: absolute; left: -150px; top: 30px;
    width: 390px; height: 390px; border-radius: 50%;
    background: radial-gradient(circle at 60% 40%, var(--brand-blue-bright), var(--brand-blue));
  }
  .contact-block {
    position: absolute; right: 30px; top: 62px;
    text-align: right;
  }
  .person-name {
    font-family: "Montserrat", sans-serif; font-weight: 700;
    font-size: 20px; color: var(--brand-blue); letter-spacing: 0.5px;
  }
  .person-role {
    font-family: "Roboto", sans-serif; font-size: 13px;
    color: var(--muted-grey); margin-top: 2px;
  }
  .contact-list { list-style: none; margin-top: 18px; }
  .contact-item {
    display: flex; justify-content: flex-end; align-items: center; gap: 8px;
    font-family: "Roboto", sans-serif; font-size: 14px; color: var(--ink-grey);
    line-height: 22px;
  }
  .contact-icon { width: 14px; height: 14px; flex: none; }
  .front-wordmark {
    position: absolute; right: 30px; bottom: 40px;
    font-family: "Montserrat", sans-serif; font-weight: 700;
    font-size: 34px; letter-spacing: 1.5px; color: var(--brand-blue);
  }
</style>
</head>
<body>
<main class="canvas">
  <section class="card card-back" aria-label="Card reverse">
    <span class="back-mark" aria-hidden="true"></span>
    <span class="back-wordmark">TALKBLOOM</span>
  </section>

  <section class="card card-front" aria-label="Card front">
    <div class="front-decoration" aria-hidden="true"></div>

    <div class="contact-block">
      <p class="person-name">OWEN HALE</p>
      <p class="person-role">CEO/FOUNDER</p>
      <ul class="contact-list">
        <li class="contact-item">712 508 3946
          <svg class="contact-icon" viewBox="0 0 14 14" aria-hidden="true"><rect x="3.5" y="1" width="7" height="12" rx="1.2" fill="none" stroke="#1b7fbf" stroke-width="1.4"/><circle cx="7" cy="11" r="0.8" fill="#1b7fbf"/></svg>
        </li>
        <li class="contact-item">Info@talkbloom.co.uk
          <svg class="contact-icon" viewBox="0 0 14 14" aria-hidden="true"><rect x="1" y="3" width="12" height="8" fill="#1b7fbf"/><path d="M1 3 L7 8 L13 3" fill="none" stroke="#fff" stroke-width="1.2"/></svg>
        </li>
        <li class="contact-item">www.talkbloom.co.uk
          <svg class="contact-icon" viewBox="0 0 14 14" aria-hidden="true"><circle cx="7" cy="7" r="6" fill="#1b7fbf"/><ellipse cx="7" cy="7" rx="2.5" ry="6" fill="none" stroke="#fff" stroke-width="1"/><line x1="1" y1="7" x2="13" y2="7" stroke="#fff" stroke-width="1"/></svg>
        </li>
      </ul>
    </div>

    <p class="front-wordmark">TALKBLOOM</p>
  </section>
</main>
</body>
</html>
```